Creative Alcoholic Beverage Package Design Needed!

We need a packaging design for a new alcoholic beverage, including the brand name. Flavours will include Sangria and Margarita, and future line extensions as well. Package will be a box (see attached dieline and example of a competitive product) in a 3 liter format. The dimensions of the box need to match the dieline, but we can be creative on the printing of the box. The product inside will be of high-quality, so the design needs to match this
Updates

Need extra days to review

Target Market(s)

25 to 40 year old, 70% female, 30% male

Colors

Requirements
Must have
• Be attractive, colourful, modern
• clearly mention the flavour, and show the components of the flavour (Sangria : red wine and citrus) - Margarita (mexican inspiration, lime, etc.)
• Have a clear "brand name" along with the flavours
• Mention the quantity (3 liters), alcohol level : 10% alc./vol.

```html
<!DOCTYPE html>
<html lang="en">
<head>
<meta charset="utf-8">
<title>Château Valentina Margarita – 3 L Box Dieline</title>
<link rel="stylesheet" href="https://fonts.googleapis.com/css2?family=Cinzel:wght@400;600&display=swap">
<style>
  :root {
    --canvas: #ececec;
    --paper: #ffffff;
    --gold: #c9a46a;
    --tan: #dbbb8e;
    --ink: #111111;
    --label-dark: #1f1c1a;
    --fold: #e0202a;
    --cut: #2b2b96;
    --wine-light: #efe2cf;
    --wine-mid: #cfae84;
  }
  html, body {
    margin: 0;
    width: 1200px;
    height: 1200px;
    overflow: hidden;
    background: var(--canvas);
  }
  .dieline {
    display: block;
    width: 1200px;
    height: 1200px;
    font-family: "Cinzel", serif;
  }
  .sheet { fill: var(--paper); }
  .base-band { fill: var(--tan); }
  .cut-line { fill: none; stroke: var(--cut); stroke-width: 1.4; }
  .fold-line { fill: none; stroke: var(--fold); stroke-width: 1.2; }
  .perforation { stroke: var(--cut); stroke-width: 1.2; stroke-dasharray: 5 7; }
  .brand-top { fill: var(--ink); }
  .brand-name { fill: var(--ink); }
  .brand-rule { stroke: var(--gold); stroke-width: 2; }
  .gold-num { fill: var(--gold); font-size: 40px; }
  .unit { fill: var(--label-dark); font-size: 15px; }
  .flavour-bar { fill: var(--gold); }
  .flavour-name { fill: var(--ink); font-size: 31px; }
  .flavour-sub-bar { fill: var(--label-dark); }
  .flavour-sub { fill: #ffffff; font-size: 12.5px; letter-spacing: 0.5px; }
  .note-bar { fill: var(--gold); }
  .note-head { fill: var(--ink); font-size: 9px; }
  .note-text { fill: var(--ink); font-size: 9px; }
  .scale-line { stroke: var(--ink); stroke-width: 4; }
  .scale-mark { fill: var(--ink); }
  .scale-label { fill: var(--ink); font-size: 7.5px; }
  .serve { fill: var(--ink); font-size: 8.5px; }
</style>
</head>
<body>
<svg class="dieline" viewBox="0 0 1280 1280" xmlns="http://www.w3.org/2000/svg">
  <defs>
    <radialGradient id="wine-splash" cx="50%" cy="55%" r="60%">
      <stop offset="0%" stop-color="var(--wine-mid)"/>
      <stop offset="55%" stop-color="var(--wine-light)"/>
      <stop offset="100%" stop-color="#ffffff" stop-opacity="0"/>
    </radialGradient>

    <!-- Main panel (front / back) -->
    <g id="main-panel">
      <g role="img" aria-label="Photo of a wine glass with pale margarita wine splashing out">
        <rect x="360" y="520" width="310" height="470" rx="120" fill="url(#wine-splash)"/>
      </g>
      <text class="brand-top" x="483" y="446" font-size="26" text-anchor="middle">CHÂTEAU</text>
      <text class="brand-name" x="483" y="499" font-size="48" text-anchor="middle" textLength="300" lengthAdjust="spacingAndGlyphs">VALENTINA</text>
      <line class="brand-rule" x1="330" y1="510" x2="636" y2="510"/>
      <rect class="flavour-bar" x="300" y="670" width="207" height="40"/>
      <text class="flavour-name" x="403" y="703" text-anchor="middle" textLength="198" lengthAdjust="spacingAndGlyphs">MARGARITA</text>
      <rect class="flavour-sub-bar" x="300" y="710" width="207" height="23"/>
      <text class="flavour-sub" x="403" y="726" text-anchor="middle">MEXICAN INSPIRATION, LIME</text>
      <text class="gold-num" x="346" y="868" text-anchor="middle">3</text>
      <text class="unit" x="347" y="888" text-anchor="middle">LITRES</text>
      <text class="gold-num" x="606" y="868" text-anchor="middle">10%</text>
      <text class="unit" x="609" y="888" text-anchor="middle">ALC./VOL</text>
    </g>

    <!-- Side panel -->
    <g id="side-panel">
      <g role="img" aria-label="Photo of a tilted wine glass with pale wine splashing">
        <rect x="130" y="600" width="168" height="340" rx="70" fill="url(#wine-splash)"/>
      </g>
      <text class="brand-top" x="208" y="434" font-size="12" text-anchor="middle">CHÂTEAU</text>
      <text class="brand-name" x="208" y="460" font-size="24" text-anchor="middle" textLength="146" lengthAdjust="spacingAndGlyphs">VALENTINA</text>
      <rect class="note-bar" x="134" y="511" width="145" height="11"/>
      <text class="note-head" x="208" y="520" text-anchor="middle">TASTING NOTES</text>
      <text class="note-text" x="208" y="532" text-anchor="middle">A PLEASING MEXICAN</text>
      <text class="note-text" x="208" y="542" text-anchor="middle">INSPIRATION, LIME .</text>
      <rect class="note-bar" x="134" y="552" width="145" height="11"/>
      <text class="note-head" x="208" y="561" text-anchor="middle">BODY</text>
      <line class="scale-line" x1="134" y1="576" x2="279" y2="576"/>
      <path class="scale-mark" d="M138,568h8l-4,5z M204,568h8l-4,5z M271,568h8l-4,5z"/>
      <text class="scale-label" x="135" y="593">LIGHT</text>
      <text class="scale-label" x="208" y="593" text-anchor="middle">MEDIUM</text>
      <text class="scale-label" x="285" y="593" text-anchor="end">FULL</text>
      <rect class="note-bar" x="134" y="611" width="145" height="11"/>
      <text class="note-head" x="208" y="620" text-anchor="middle">SWEETNESS</text>
      <line class="scale-line" x1="134" y1="635" x2="279" y2="635"/>
      <path class="scale-mark" d="M146,627h8l-4,5z M184,627h8l-4,5z M226,627h8l-4,5z M264,627h8l-4,5z"/>
      <text class="scale-label" x="150" y="649" text-anchor="middle">DRY</text>
      <text class="scale-label" x="188" y="649" text-anchor="middle">MEDIUM</text>
      <text class="scale-label" x="188" y="658" text-anchor="middle">DRY</text>
      <text class="scale-label" x="230" y="649" text-anchor="middle">MEDIUM</text>
      <text class="scale-label" x="230" y="658" text-anchor="middle">SWEET</text>
      <text class="scale-label" x="267" y="649" text-anchor="middle">SWEET</text>
      <text class="serve" x="135" y="676">SERVE AT ROOM TEMPERATURE</text>
      <!-- top flap with finger notch -->
      <path class="cut-line" d="M120,376 V276 Q120,260 136,260 H160 Q168,260 168,268 A38,38 0 0 0 244,268 Q244,260 252,260 H274 Q290,260 290,276 V376"/>
      <!-- bottom flap -->
      <path class="cut-line" d="M120,903 V1036 Q120,1052 136,1052 H274 Q290,1052 290,1036 V903"/>
      <line class="perforation" x1="135" y1="280" x2="150" y2="350"/>
      <line class="perforation" x1="268" y1="280" x2="280" y2="350"/>
      <line class="perforation" x1="135" y1="1030" x2="150" y2="920"/>
      <line class="perforation" x1="268" y1="1030" x2="280" y2="920"/>
    </g>
  </defs>

  <!-- sheet and base colour band -->
  <rect class="sheet" x="46" y="183" width="1189" height="912"/>
  <rect class="base-band" x="109" y="903" width="1113" height="192"/>

  <!-- panels -->
  <use href="#side-panel"/>
  <use href="#side-panel" transform="translate(555 0)"/>
  <use href="#main-panel"/>
  <use href="#main-panel" transform="translate(555 0)"/>

  <!-- glue flap -->
  <path class="cut-line" d="M112,383 L62,395 V1044 Q62,1052 70,1052 H112"/>
  <line class="fold-line" x1="62" y1="888" x2="118" y2="888"/>
  <line class="fold-line" x1="62" y1="910" x2="118" y2="910"/>
  <line class="perforation" x1="80" y1="410" x2="100" y2="410" stroke-dasharray="none"/>
  <line class="perforation" x1="90" y1="400" x2="90" y2="1040" stroke-dasharray="6 20"/>

  <!-- front handle flap -->
  <path class="cut-line" d="M305,376 V220 Q305,198 327,198 H642 Q664,198 664,220 V376"/>
  <rect class="cut-line" x="406" y="260" width="156" height="50" rx="25"/>
  <path class="cut-line" d="M305,903 V1058 Q305,1080 327,1080 H642 Q664,1080 664,1058 V903"/>

  <!-- back handle flap -->
  <path class="cut-line" d="M862,376 V220 Q862,198 884,198 H1198 Q1220,198 1220,220 V376"/>
  <rect class="cut-line" x="955" y="253" width="171" height="58" rx="22"/>
  <line class="fold-line" x1="975" y1="253" x2="1106" y2="253"/>
  <path class="cut-line" d="M862,903 V1058 Q862,1080 884,1080 H1198 Q1220,1080 1220,1058 V903"/>
  <g class="back-perfs">
    <line class="perforation" x1="918" y1="215" x2="1015" y2="238"/>
    <line class="perforation" x1="1068" y1="215" x2="1165" y2="238"/>
    <line class="perforation" x1="918" y1="330" x2="1015" y2="353"/>
    <line class="perforation" x1="1068" y1="330" x2="1165" y2="353"/>
    <line class="perforation" x1="918" y1="1058" x2="1015" y2="1035"/>
    <line class="perforation" x1="1068" y1="1058" x2="1165" y2="1035"/>
    <line class="perforation" x1="1068" y1="942" x2="1165" y2="920"/>
  </g>

  <!-- pour spout window on second side -->
  <path class="cut-line" d="M712,706 V840 M814,706 V840" stroke-dasharray="3 3"/>
  <line class="fold-line" x1="712" y1="706" x2="814" y2="706"/>
  <rect class="cut-line" x="732" y="792" width="60" height="50" stroke-dasharray="3 3"/>

  <!-- fold lines -->
  <line class="fold-line" x1="118" y1="376" x2="1222" y2="376"/>
  <line class="fold-line" x1="118" y1="903" x2="1222" y2="903"/>
  <line class="fold-line" x1="118" y1="376" x2="118" y2="903"/>
  <line class="fold-line" x1="298" y1="376" x2="298" y2="903"/>
  <line class="fold-line" x1="668" y1="376" x2="668" y2="903"/>
  <line class="fold-line" x1="855" y1="376" x2="855" y2="903"/>
  <line class="cut-line" x1="1222" y1="376" x2="1222" y2="903"/>
</svg>
</body>
</html>
```